IT services company needs a business card designed

-2 sided business card.-Front is going to be the logo raised (3D floating effect) on a black background. Make the logos spider web shiny silver and keep the spider the same design. -Back needs to have the following information:Darrel Sotho, Managing Partner, Cell: 738-402-1954, Website: Plankhorn.com, Email: Darrel@Plankhorn.com
Target Market(s)
IT Services
Industry/Entity Type
It Company
Contact Information for Business Card
-2 sided business card.
-Front is going to be the logo raised (3D floating effect) on a black background. Make the logos spider web shiny silver and keep the spider the same design.
-Back needs to have the following information:
Darrel Sotho, Managing Partner, Cell: 738-402-1954, Website: Plankhorn.com, Email: Darrel@Plankhorn.com

```html
<!DOCTYPE html>
<html lang="en">
<head>
<meta charset="utf-8">
<title>Plankhorn – Business Card</title>
<link href="https://fonts.googleapis.com/css2?family=Questrial&display=swap" rel="stylesheet">
<style>
  :root {
    --page-bg: #ececec;
    --card-dark: #212021;
    --card-light: #ffffff;
    --brand-blue: #00b0e8;
    --brand-blue-deep: #0a9fd6;
    --rule-blue: #6fd0f2;
    --ink-grey: #4a4747;
    --silver: #cfcfcf;
    --mark-silver: #8f8f8f;
    --mark-blue: #5cc4ea;
    --white: #ffffff;
  }
  * { box-sizing: border-box; margin: 0; padding: 0; }
  html, body { width: 1200px; height: 1200px; overflow: hidden; }
  body {
    background: var(--page-bg);
    font-family: "Questrial", sans-serif;
    position: relative;
  }
  .card {
    position: absolute;
    top: 192px;
    width: 474px;
    height: 808px;
    overflow: hidden;
  }
  .card--front { left: 75px; background: var(--card-dark); }
  .card--back { left: 645px; background: var(--card-light); }

  .front-band {
    position: absolute; left: 0; right: 0; bottom: 0;
    height: 16px; background: var(--brand-blue);
  }
  .back-band {
    position: absolute; left: 0; right: 0; top: 0;
    height: 19px; background: var(--brand-blue);
  }

  .brand-mark {
    position: absolute;
    border-radius: 50%;
  }
  .card--front .brand-mark {
    left: 133px; top: 257px; width: 210px; height: 210px;
    background: var(--mark-silver);
  }
  .card--back .brand-mark {
    left: 127px; top: 124px; width: 220px; height: 220px;
    background: var(--mark-blue);
  }

  .brand-name {
    position: absolute; left: 0; right: 0;
    text-align: center;
    font-size: 56px;
    letter-spacing: 1px;
    line-height: 1;
  }
  .card--front .brand-name { top: 491px; color: var(--silver); }
  .card--back .brand-name { top: 367px; color: var(--ink-grey); }

  .contact-panel {
    position: absolute; left: 0; right: 0; bottom: 0;
    height: 272px;
    background: linear-gradient(180deg, var(--brand-blue-deep), var(--brand-blue));
    color: var(--white);
  }
  .contact-row {
    display: flex; align-items: center;
    border-bottom: 1.5px solid var(--rule-blue);
    padding-left: 42px;
  }
  .contact-row:last-child { border-bottom: none; }
  .contact-row--name { height: 98px; align-items: flex-start; padding-top: 16px; }
  .contact-row--line { height: 58px; }
  .contact-icon { width: 28px; height: 28px; flex: none; margin-right: 22px; }
  .contact-row--name .contact-icon { margin-top: 4px; }
  .person-name { font-size: 30px; line-height: 1.1; }
  .person-title { font-size: 23px; margin-top: 6px; }
  .contact-text { font-size: 23px; }
</style>
</head>
<body>
  <section class="card card--front" aria-label="Card front">
    <div class="brand-mark" role="img" aria-label="Company mark"></div>
    <div class="brand-name">PLANKHORN</div>
    <div class="front-band"></div>
  </section>

  <section class="card card--back" aria-label="Card back">
    <div class="back-band"></div>
    <div class="brand-mark" role="img" aria-label="Company mark"></div>
    <div class="brand-name">PLANKHORN</div>

    <div class="contact-panel">
      <div class="contact-row contact-row--name">
        <svg class="contact-icon" viewBox="0 0 28 28" aria-hidden="true">
          <circle cx="14" cy="14" r="12" fill="none" stroke="#fff" stroke-width="1.6"/>
          <circle cx="14" cy="11" r="3.4" fill="#fff"/>
          <path d="M8 20c1-3.5 3.2-5 6-5s5 1.5 6 5z" fill="#fff"/>
        </svg>
        <div>
          <div class="person-name">Darrel Sotho</div>
          <div class="person-title">Managing Partner</div>
        </div>
      </div>
      <div class="contact-row contact-row--line">
        <svg class="contact-icon" viewBox="0 0 28 28" aria-hidden="true">
          <circle cx="14" cy="14" r="12" fill="none" stroke="#fff" stroke-width="1.6"/>
          <path d="M10 8.5c-1.5 1-1.8 3 0 6s3.8 4.6 6.2 5.2c1.6.4 2.6-.4 3.2-1.4l-2.4-2-1.6 1c-1.4-.6-3-2.4-3.6-3.8l1-1.6z" fill="none" stroke="#fff" stroke-width="1.4" stroke-linejoin="round"/>
        </svg>
        <div class="contact-text">738-402-1954</div>
      </div>
      <div class="contact-row contact-row--line">
        <svg class="contact-icon" viewBox="0 0 28 28" aria-hidden="true">
          <circle cx="14" cy="14" r="12" fill="none" stroke="#fff" stroke-width="1.6"/>
          <rect x="8.5" y="10" width="11" height="8" fill="none" stroke="#fff" stroke-width="1.4"/>
          <path d="M8.5 10l5.5 4.5 5.5-4.5" fill="none" stroke="#fff" stroke-width="1.4"/>
        </svg>
        <div class="contact-text">Darrel@Plankhorn.com</div>
      </div>
      <div class="contact-row contact-row--line">
        <svg class="contact-icon" viewBox="0 0 28 28" aria-hidden="true">
          <circle cx="14" cy="14" r="12" fill="none" stroke="#fff" stroke-width="1.6"/>
          <path d="M11 8v11l2.6-2.4 1.8 3.6 1.6-.8-1.8-3.5 3.4-.3z" fill="#fff"/>
        </svg>
        <div class="contact-text">www.Plankhorn.com</div>
      </div>
    </div>
  </section>
</body>
</html>
```